Kaluvo - Adventurous, Fun, Exciting, Social Fitness Club needs a Webpage with attitude!

Kaluvo... we're a fun, social, outdoor fitness club that needs not just a homepage designed for our website, but in the process a "personality" for our unique, innovative and cheeky brand.
We pride ourselves on getting our members outdoors trying new, exciting physical activities in an effort to find joy in an active lifestyle, and sharing that experience with other like minded people. We offer:
- Personal Training (1-on-1 Fitness Training)
- Group Fitness Classes (Boxing, Pilates, etc)
- Boot Camps (Military Style - Sandbags, Ropes, Tyres, etc)
- Events (Fun Runs, Triathlons, Ocean Swims, Treks, etc)
- Adventures(Machu Picchu Trek, Rock Climbing, Kayaking, etc)
Our tag line is 'No Judgements. No Limits!' The homepage should be exciting, adventurous and innovative, illustrating the values of our brand: possibility, thirst for life, personal accomplishment & freedom. It should be fun, friendly & inviting.
A few of our key benefits to members are:
- No Boring Workouts
- No Joining Fees or Long Term Contracts
- Results Guaranteed
The links below should give you a rough idea of the sort of "feel" we're after (vibrant, active, adventurous ).
http://www.pupiljourneys.com.au/
http://www.layoutgoblin.com/website-templates/31924.html
http://www.layoutgoblin.com/website-templates/32751.html
http://www.pivel.com/
Target Market(s)
Real, Everyday People - Men & Women (30:70) aged mainly between 21-40, who want a more exciting and enjoyable fitness experience than your typical gym offers.
Industry/Entity Type
Fitness
Requirements
Must have
- Strong, uplifting and motivating images of people enjoying fitness/physical activities outdoors

```html
<!DOCTYPE html>
<html lang="en">
<head>
<meta charset="utf-8">
<title>Kaluvo – Outdoor Fitness Club</title>
<link rel="stylesheet" href="https://fonts.googleapis.com/css2?family=Arimo:wght@400;700&family=Kaushan+Script&family=Open+Sans:wght@400;700&family=Oswald:wght@400;500&display=swap">
<style>
:root{
  --orange:#f07a12;
  --orange-dark:#d9620a;
  --ink:#222;
  --text:#444;
  --muted:#555;
  --white:#fff;
  --nav-top:#5a5a5a;
  --nav-bottom:#2c2c2c;
  --footer:#3a3230;
}
*{box-sizing:border-box;margin:0;padding:0}
html,body{width:1100px;height:1200px;overflow:hidden}
body{position:relative;background:var(--white);font-family:Arimo,Arial,sans-serif;color:var(--text)}
.abs{position:absolute}

/* header */
.site-header{left:0;top:0;width:1100px;height:131px;background:var(--white)}
.brand{left:62px;top:42px;font:700 46px/1 "Open Sans",sans-serif;color:var(--orange);letter-spacing:1px;display:flex;align-items:center;gap:12px}
.brand-dot{width:18px;height:18px;border-radius:50%;background:var(--ink)}
.contact-box{left:808px;top:12px;width:226px;height:90px;border-radius:6px;background:linear-gradient(#4a4a4a,#262626);box-shadow:0 2px 4px rgba(0,0,0,.3)}
.contact-phone{left:16px;top:14px;display:flex;align-items:center;gap:8px;color:var(--white);font:400 22px/1 Arimo,sans-serif;letter-spacing:1px}
.club-btn{left:8px;top:57px;width:123px;height:22px;border-radius:3px;background:#3d3d3d;color:#eee;font-size:11px;display:flex;align-items:center;gap:6px;padding-left:8px}
.login{left:158px;top:61px;color:#ddd;font-size:12px;letter-spacing:.5px}
.login::before{content:"";display:inline-block;border-left:5px solid var(--orange);border-top:4px solid transparent;border-bottom:4px solid transparent;margin-right:5px}

/* nav */
.main-nav{left:0;top:131px;width:1100px;height:40px;background:linear-gradient(var(--nav-top),var(--nav-bottom))}
.nav-item{top:0;height:40px;color:var(--white);font:400 11.5px/40px "Open Sans",sans-serif;text-transform:uppercase;letter-spacing:-.2px}
.nav-item.active{top:6px;height:26px;line-height:26px;padding:0 16px;border-radius:4px;background:linear-gradient(#fb9a35,var(--orange-dark))}
.nav-sep{top:9px;width:1px;height:22px;background:#777}

/* backdrop */
.backdrop{left:0;top:171px;width:1100px;height:929px;background:linear-gradient(100deg,#93aee0 0%,#c8d6f1 35%,#d6dcea 55%,#9aa0a2 80%,#7c8a5e 100%)}

/* slider */
.slider{left:75px;top:192px;width:606px;height:304px;background:var(--white);padding:6px;box-shadow:0 1px 3px rgba(0,0,0,.3)}
.slide-img{left:6px;top:6px;width:592px;height:291px;background:linear-gradient(90deg,#6d4a2a 0%,#a87a48 25%,#e6b75a 55%,#f0c866 75%,#8c6a3e 100%)}
.slide-caption{right:22px;text-align:right;white-space:nowrap}
.cap-dark{font:400 30px/1 Georgia,serif;color:#1b1410;letter-spacing:1px}
.cap-orange{font:700 33px/1 Georgia,serif;color:var(--orange);-webkit-text-stroke:1px #fff}
.slide-bar{left:6px;top:256px;width:592px;height:41px;background:rgba(30,30,30,.55)}
.dot{top:13px;width:11px;height:11px;border-radius:50%;background:var(--white)}
.dot.on{background:var(--orange)}

/* membership */
.join{left:704px;top:193px;width:297px;height:305px;background:linear-gradient(135deg,#fff 70%,#fde9c8 85%,#e84f8a 100%);box-shadow:0 1px 3px rgba(0,0,0,.3)}
.join-title{left:11px;top:12px;font:500 22px/1 Oswald,sans-serif;color:var(--orange);letter-spacing:.5px;text-transform:uppercase;white-space:nowrap}
.perks{left:8px;top:50px;list-style:none}
.perks li{display:flex;align-items:center;gap:8px;height:28px;font:400 16px/1 Oswald,sans-serif;color:var(--ink);white-space:nowrap}
.field-label{left:12px;font:500 15px/1 Oswald,sans-serif;color:var(--ink)}
.field{left:56px;width:172px;height:24px;border:1px solid #999;background:var(--white)}
.join-btn{left:169px;top:255px;width:96px;height:34px;border-radius:8px;background:linear-gradient(#333,#000);border:2px solid #888;color:var(--white);font:400 17px/30px Oswald,sans-serif;text-align:center;letter-spacing:1px}

/* service cards */
.card{top:520px;height:305px;background:var(--white);box-shadow:0 1px 3px rgba(0,0,0,.3)}
.card-img{left:11px;top:8px;width:268px;height:139px}
.card-title{left:14px;font:700 16px/1 "Open Sans",sans-serif;color:#3c3c3c;text-transform:uppercase;letter-spacing:.3px;white-space:nowrap}
.card-text{left:12px;width:256px;font:400 11px/18px Arimo,sans-serif;color:var(--text);letter-spacing:.35px}
.more{right:20px;top:262px;font:700 12px/1 Arimo,sans-serif;color:var(--text);white-space:nowrap}
.more::before{content:"";display:inline-block;border-left:4px solid var(--text);border-top:3px solid transparent;border-bottom:3px solid transparent;margin-right:5px;vertical-align:1px}

/* seo section */
.seo{left:76px;top:855px;width:922px;height:240px;background:var(--white)}
.seo-tab{left:-9px;top:2px;width:318px;height:44px;background:var(--orange);color:var(--white);display:flex;align-items:center;gap:10px;padding-left:20px;font:400 17px/1 "Open Sans",sans-serif;letter-spacing:.5px;white-space:nowrap}
.seo-tab em{font:400 22px/1 "Kaushan Script",cursive;font-style:normal}
.seo-list{left:16px;top:66px;list-style:none}
.seo-list li{height:22px;font:400 12px/1 Arimo,sans-serif;color:var(--text);letter-spacing:.3px;padding-left:14px;position:relative;white-space:nowrap}
.seo-list li::before{content:"";position:absolute;left:0;top:2px;border-left:4px solid var(--text);border-top:3px solid transparent;border-bottom:3px solid transparent}
.video{left:590px;top:21px;width:312px;height:196px;border-radius:8px;background:#9a9a9a;box-shadow:0 2px 4px rgba(0,0,0,.4);overflow:hidden}
.video-screen{left:3px;top:3px;width:306px;height:170px;background:linear-gradient(160deg,#0e2a6e,#2f6ad0 50%,#0b1d4d)}
.play{left:121px;top:62px;width:74px;height:74px;border-radius:8px;background:rgba(200,200,200,.75)}
.video-bar{left:0;top:175px;width:312px;height:21px;background:linear-gradient(#bdbdbd,#8a8a8a)}

/* footer */
.site-footer{left:0;top:1100px;width:1100px;height:100px;background:var(--footer)}
.legal{left:0;top:38px;width:1040px;text-align:center;color:var(--white);font:400 11px/18px Arimo,sans-serif}
.footer-brand{left:895px;top:42px;font:700 30px/1 "Open Sans",sans-serif;color:#6b6361}
</style>
</head>
<body>

<header class="site-header abs">
  <div class="brand abs"><span class="brand-dot"></span>Kaluvo</div>
  <div class="contact-box abs">
    <div class="contact-phone abs">
      <svg width="30" height="30" viewBox="0 0 30 30"><rect x="2" y="2" width="26" height="26" rx="6" fill="#f0a020"/><path d="M10 8c1-1 2 0 3 2s0 2-1 3c1 2 3 4 5 5 1-1 1-2 3-1s3 2 2 3c-1 2-3 3-6 1-3-2-6-5-7-8-1-2 0-4 1-5z" fill="#fff"/></svg>
      1300 555 017
    </div>
    <div class="club-btn abs">
      <svg width="12" height="14" viewBox="0 0 12 14"><path d="M6 0a5 5 0 0 1 5 5c0 4-5 9-5 9S1 9 1 5a5 5 0 0 1 5-5z" fill="#f0a020"/><circle cx="6" cy="5" r="2" fill="#3d3d3d"/></svg>
      Club Location ▸
    </div>
    <div class="login abs">Login</div>
  </div>
</header>

<nav class="main-nav abs">
  <a class="nav-item active abs" style="left:89px">Home</a>
  <span class="nav-sep abs" style="left:169px"></span>
  <a class="nav-item abs" style="left:189px">About Us</a>
  <span class="nav-sep abs" style="left:266px"></span>
  <a class="nav-item abs" style="left:295px">Fitness</a>
  <span class="nav-sep abs" style="left:361px"></span>
  <a class="nav-item abs" style="left:388px">Events &amp; Adventures</a>
  <span class="nav-sep abs" style="left:535px"></span>
  <a class="nav-item abs" style="left:557px">Contact Us</a>
</nav>

<div class="backdrop abs" role="img" aria-label="Mountain landscape with blue sky and a rock face"></div>

<section class="slider abs">
  <div class="slide-img abs" role="img" aria-label="Climber on a rock face against a golden sunset sky"></div>
  <p class="slide-caption cap-dark abs" style="top:124px">your body secretes</p>
  <p class="slide-caption cap-orange abs" style="top:164px;right:28px">endorphins which relieves</p>
  <p class="slide-caption cap-dark abs" style="top:205px;font-size:27px">the nervous tension.</p>
  <div class="slide-bar abs">
    <span class="dot abs" style="left:500px"></span>
    <span class="dot on abs" style="left:519px"></span>
    <span class="dot abs" style="left:539px"></span>
    <span class="dot abs" style="left:559px"></span>
  </div>
</section>

<aside class="join abs">
  <h2 class="join-title abs">Free Membership, Join Us</h2>
  <ul class="perks abs">
    <li><svg width="14" height="12" viewBox="0 0 14 12"><path d="M1 6l4 4 8-9" stroke="#f07a12" stroke-width="3" fill="none"/></svg>Monthly E-News Hints, tips &amp; Advice</li>
    <li><svg width="14" height="12" viewBox="0 0 14 12"><path d="M1 6l4 4 8-9" stroke="#f07a12" stroke-width="3" fill="none"/></svg>VIP Invites Events &amp; Adventures</li>
    <li><svg width="14" height="12" viewBox="0 0 14 12"><path d="M1 6l4 4 8-9" stroke="#f07a12" stroke-width="3" fill="none"/></svg>Special Member only offers</li>
    <li><svg width="14" height="12" viewBox="0 0 14 12"><path d="M1 6l4 4 8-9" stroke="#f07a12" stroke-width="3" fill="none"/></svg>Discounts Cards to 20+ Providers</li>
  </ul>
  <span class="field-label abs" style="top:186px">Name:</span>
  <span class="field abs" style="top:181px"></span>
  <span class="field-label abs" style="top:218px">Email:</span>
  <span class="field abs" style="top:214px"></span>
  <span class="join-btn abs">Join Us</span>
</aside>

<article class="card abs" style="left:75px;width:288px">
  <div class="card-img abs" role="img" aria-label="Trainer helping a woman lift dumbbells" style="background:linear-gradient(120deg,#2a2a2a,#e8743a 45%,#c9a07a 70%,#1d1d1d)"></div>
  <h3 class="card-title abs" style="top:159px">Personal Traning</h3>
  <p class="card-text abs" style="top:187px">Lorem Ipsum is simply dummy text of the printing and typesetting industry. Lorem Ipsum has been the industry's standard dummy text took a galley of t to make a type specimen book</p>
  <span class="more abs">more details...</span>
</article>

<article class="card abs" style="left:393px;width:287px">
  <div class="card-img abs" role="img" aria-label="Group fitness class exercising on mats in a park" style="left:10px;width:266px;background:linear-gradient(#6f9a3c,#4f8a2e 60%,#3d6e24)"></div>
  <h3 class="card-title abs" style="top:158px;left:12px">Group Fitness</h3>
  <p class="card-text abs" style="top:179px">Lorem Ipsum is simply dummy text of the printing and typesetting industry. Lorem Ipsum has been the industry's standard dummy text took a galley of t to make a type specimen book</p>
  <span class="more abs" style="right:26px">more details...</span>
</article>

<article class="card abs" style="left:712px;width:287px">
  <div class="card-img abs" role="img" aria-label="Camper van and boots on a grassy field" style="left:9px;background:linear-gradient(#bcd3e8,#d88a4a 45%,#6e9a3a 70%,#3e6a26)"></div>
  <h3 class="card-title abs" style="top:158px;left:8px">Boot Camp</h3>
  <p class="card-text abs" style="top:179px;left:10px">Lorem Ipsum is simply dummy text of the printing and typesetting industry. Lorem Ipsum has been the industry's standard dummy text took a galley of t to make a type specimen book</p>
  <span class="more abs" style="right:26px">more details...</span>
</article>

<section class="seo abs">
  <h2 class="seo-tab abs"><em>SEO Copy</em> -PERSONAL TRAINING</h2>
  <ul class="seo-list abs">
    <li>Introduction to the core search ranking&nbsp; he core search ranking&nbsp; he core ranking factors</li>
    <li>Keyphrase selection -&nbsp; he core search ranking&nbsp; techniques and tools</li>
    <li>Psychology of he core search ranking&nbsp; user search behaviour and user journeys</li>
    <li>Competitor benchmarking he core search ranking&nbsp; techniques and tools</li>
    <li>The importance of web analytics&nbsp; he core search ranking and goal tracking</li>
    <li>Psychology of user search behaviour and user journeys</li>
    <li>Competitor benchmarking techniques and tools</li>
  </ul>
  <div class="video abs">
    <div class="video-screen abs" role="img" aria-label="Video still of ice hockey players on the rink"></div>
    <svg class="play abs" viewBox="0 0 74 74"><path d="M28 20l26 17-26 17z" fill="#111"/></svg>
    <div class="video-bar abs">
      <svg width="312" height="21" viewBox="0 0 312 21">
        <rect x="8" y="5" width="72" height="11" rx="5" fill="#777"/>
        <rect x="84" y="9" width="170" height="3" fill="#666"/>
        <rect x="262" y="9" width="40" height="3" fill="#666"/>
      </svg>
    </div>
  </div>
</section>

<footer class="site-footer abs">
  <p class="legal abs">© Northway Travel Group trading as Pupil Journeys ABN 41 902 115 630 ACN 902 115 630 Travel<br>Providers of student travel, cheap flights, cheap hotels, round the world flights and more.<br>Read more: Cheap Flights for Everyone | Budget and Student Travel Experts</p>
  <span class="footer-brand abs">Kaluvo</span>
</footer>

</body>
</html>
```